Bold Website Design for Fitness Trainer - No Coding

We are in need of a bold and unique website design for a personal fitness training company, www.TessaLorvel.com. We need DESIGN ONLY for three pages. These will be a homepage, a lead capture page, and one internal page with a sidebar. The design will be used for coding a wordpress theme, if that matters for the designer.

Tessa Lorvel Fitness Training
2738 E 19th St #415
Austin, TX 78705
512-607-4918
http://www.tessalorvel.com

Target Market(s)

18-45 year old male and females making 80k+ a year and looking to get stronger and in shape.

Industry/Entity Type

Fitness

Number of Pages Required

3 page

Font styles to use
Sans Serif

Requirements
Must have
• See attached design specs file.
Nice to have
Should not have
• Boxed layout.
• Dark Background.

```html
<!DOCTYPE html>
<html lang="en">
<head>
<meta charset="utf-8">
<title>Tessa Lorvel Fitness Training</title>
<link href="https://fonts.googleapis.com/css2?family=Audiowide&family=Montserrat:wght@400;600;700&family=Open+Sans:ital,wght@0,400;0,600;0,700;1,600&display=swap" rel="stylesheet">
<style>
:root{
  --cyan:#4ec3dc;
  --cyan-dark:#36a9c2;
  --pink:#e8318f;
  --yellow:#f5e11c;
  --ink:#2b2b2b;
  --text:#555;
  --muted:#8a8a8a;
  --line:#dcdcdc;
  --grey-bg:#f1f1f1;
  --footer:#2a2a2c;
  --topbar:#262626;
}
*{box-sizing:border-box;margin:0;padding:0}
html,body{width:1200px;height:4162px;overflow:hidden}
body{font-family:"Open Sans",Arial,sans-serif;color:var(--text);background:#fff;font-size:13px}
.wrap{width:870px;margin:0 auto;position:relative}
.btn{display:inline-block;background:var(--pink);color:#fff;font-family:"Montserrat",sans-serif;font-weight:700;font-size:13px;letter-spacing:.5px;padding:13px 34px;border-radius:30px;text-transform:uppercase}
.center{text-align:center}

/* top bar */
.topbar{height:28px;background:var(--topbar);color:#bbb;font-size:10px}
.topbar .wrap{display:flex;align-items:center;height:28px;gap:22px}
.topbar .appt{border:1px solid #555;padding:2px 8px}
.topbar .social{margin-left:auto;display:flex;gap:6px}
.topbar .social span{width:14px;height:14px;border-radius:50%;background:#444;display:block}

/* header */
.header{height:187px;display:flex;align-items:center;justify-content:center;gap:18px;background:#fff}
.brand-mark{width:96px;height:96px;border-radius:50%;background:var(--yellow)}
.brand-name{font-family:"Montserrat",sans-serif;font-weight:700;font-size:46px;color:var(--cyan-dark)}

/* nav */
.nav{height:55px;background:var(--cyan)}
.nav ul{list-style:none;display:flex;justify-content:center;height:55px}
.nav li{font-family:"Montserrat",sans-serif;font-weight:600;font-size:12px;color:#fff;padding:0 34px;display:flex;align-items:center;border-right:1px solid rgba(255,255,255,.3)}
.nav li.active{background:var(--cyan-dark)}
.nav li.cta{background:var(--pink);border:none}

/* hero */
.hero{height:486px;position:relative;background:linear-gradient(90deg,#1b1b1b,#4a3f36 45%,#2a2522 70%,#141414)}
.hero .copy{position:absolute;top:140px;width:100%;text-align:center}
.hero h1{font-family:"Audiowide",sans-serif;font-weight:400;font-size:46px;color:var(--yellow);letter-spacing:2px}
.hero .sub{margin-top:26px;font-style:italic;font-weight:600;font-size:22px;color:#f2c230}
.hero .btn{margin-top:34px}
.hero .arrow{position:absolute;top:215px;width:28px;height:56px;background:rgba(255,255,255,.25)}
.hero .arrow.l{left:0}.hero .arrow.r{right:0}
.hero .dots{position:absolute;bottom:18px;width:100%;display:flex;justify-content:center;gap:7px}
.hero .dots span{width:8px;height:8px;border-radius:50%;background:rgba(255,255,255,.5)}
.hero .dots span.on{background:#fff}

/* section title */
.sec-title{display:flex;align-items:center;justify-content:center;gap:0}
.sec-title .rule{width:80px;height:1px;background:#999}
.sec-title h2{font-family:"Montserrat",sans-serif;font-weight:700;font-size:24px;color:var(--ink);padding:12px 38px;border-top:1px solid #999;border-bottom:1px solid #999;letter-spacing:1px;clip-path:polygon(6% 0,94% 0,100% 50%,94% 100%,6% 100%,0 50%)}
.sec-sub{text-align:center;color:var(--muted);font-size:13px;margin-top:14px}

/* get started */
.get-started{height:440px;background:var(--grey-bg);padding-top:52px}
.features{display:flex;justify-content:space-between;width:820px;margin:36px auto 0}
.feature{width:150px;text-align:center}
.feature .label{font-size:16px;color:#666;line-height:1.15}
.feature .label b{display:block;font-weight:600;font-size:18px;color:#555}
.feature .bowl{width:120px;height:60px;margin:8px auto 0;background:#d6d6d6;border-radius:0 0 60px 60px;display:flex;align-items:flex-start;justify-content:center;padding-top:12px}
.get-started .btn{margin-top:55px;padding:14px 40px}

/* services */
.services{height:826px;padding-top:56px}
.services .intro{width:760px;margin:22px auto 0;text-align:center;font-size:15px;color:#666;line-height:1.5}
.tabs{display:flex;justify-content:center;gap:4px;margin-top:26px}
.tabs span{font-size:10px;font-weight:600;color:#888;padding:9px 20px;background:#f2f2f2}
.tabs span.on{background:var(--cyan);color:#fff}
.cards{display:flex;justify-content:space-between;margin-top:18px}
.card{width:275px;border:1px solid #e6e6e6}
.card .ph{height:240px}
.card h3{font-family:"Montserrat",sans-serif;font-size:12px;font-weight:700;color:var(--ink);padding:12px 12px 4px;letter-spacing:.5px}
.card p{font-size:11px;color:var(--muted);padding:0 12px 10px;line-height:1.4}
.card .facts{display:grid;grid-template-columns:1fr 1fr;border-top:1px solid #eee}
.card .facts span{font-size:10px;color:#777;padding:9px 12px;display:flex;align-items:center;gap:6px;border-bottom:1px solid #eee}
.card .facts i{width:10px;height:10px;border:1.5px solid #999;border-radius:50%;display:block}
.services .btn{margin-top:28px}

/* testimonials */
.testimonials{height:198px;background:var(--cyan);text-align:center;padding-top:24px;color:#fff}
.testimonials h2{font-family:"Montserrat",sans-serif;font-weight:700;font-size:24px;letter-spacing:1px}
.testimonials p{width:640px;margin:14px auto 0;font-size:12px;line-height:1.5}
.testimonials .who{display:flex;justify-content:center;align-items:center;gap:10px;margin-top:10px;font-size:11px;font-weight:700}
.testimonials .who .av{width:40px;height:40px;border-radius:50%;background:#fff;border:3px solid rgba(255,255,255,.6)}

/* keep in touch */
.touch{height:554px;padding-top:52px;background:#fff}
.widgets{display:flex;justify-content:space-between;margin-top:36px;width:750px;margin-left:auto;margin-right:auto}
.widget{width:232px;height:232px;border:1px solid #ddd;box-shadow:0 1px 4px rgba(0,0,0,.12);font-size:11px}
.widget .bar{height:28px;background:#3b5a96;color:#fff;font-weight:700;display:flex;align-items:center;padding:0 10px}
.widget .bar.feed{background:#34608a;justify-content:center}
.stats{display:flex;justify-content:space-around;padding:8px 4px;border-bottom:1px solid #eee;text-align:center}
.stats b{display:block;font-size:16px;color:var(--ink)}
.stats span{font-size:9px;color:var(--muted)}
.grid{display:grid;grid-template-columns:repeat(3,1fr);gap:4px;padding:6px}
.grid div{height:46px}
.posttxt{padding:6px 10px;color:#3b5a96;line-height:1.3;font-size:10px}

/* blog */
.blog{height:676px;padding-top:52px}
.post{display:flex;gap:30px;margin-top:40px;width:870px}
.post .ph{width:420px;height:230px;background:linear-gradient(135deg,#7a2020,#3a2b2b 50%,#a08060)}
.post .meta{display:flex;align-items:center;gap:10px;font-size:11px;color:var(--muted)}
.post .meta .av{width:38px;height:38px;border-radius:50%;background:#d8c2b0}
.post .meta b{color:var(--ink)}
.post .stats{width:200px;border:none;justify-content:flex-start;gap:16px;padding:10px 0 0}
.post h3{font-family:"Montserrat",sans-serif;font-weight:700;font-size:30px;color:var(--ink);margin-top:14px}
.post p{font-size:11px;color:var(--muted);line-height:1.5;margin-top:8px;width:400px}
.post .more{font-size:11px;font-weight:700;color:var(--ink);margin-top:10px}
.thumbs{display:flex;justify-content:space-between;margin-top:20px}
.thumbs div{width:168px;height:110px}
.blog .btn{margin-top:28px}

/* join */
.join{height:191px;background:var(--cyan);padding-top:26px}
.join .band{width:760px;margin:0 auto;position:relative}
.join h2{font-family:"Montserrat",sans-serif;font-weight:700;font-size:22px;color:var(--ink);text-align:center;letter-spacing:1px}
.join .items{display:flex;justify-content:space-around;margin-top:14px;padding:10px 40px;border-top:1px solid rgba(255,255,255,.7);border-bottom:1px solid rgba(255,255,255,.7);clip-path:polygon(4% 0,96% 0,100% 50%,96% 100%,4% 100%,0 50%)}
.join .items span{color:#fff;font-size:12px;display:flex;align-items:center;gap:6px}
.join .items i{width:14px;height:14px;border:1.5px solid #fff;border-radius:50%;display:block}
.join .btn{margin-top:16px}

/* footer */
.footer{height:521px;background:var(--footer);color:#999;padding-top:36px}
.tags{width:650px;margin:0 auto;display:flex;flex-wrap:wrap;gap:0}
.tags span{font-size:9px;color:#bbb;border:1px solid #555;padding:6px 0;width:108px;text-align:center;letter-spacing:.5px}
.contacts{display:flex;justify-content:space-between;width:640px;margin:48px auto 0;text-align:center}
.contact .ic{width:62px;height:62px;border-radius:50%;border:2px solid #666;margin:0 auto;display:flex;align-items:center;justify-content:center}
.contact h4{font-family:"Montserrat",sans-serif;font-size:12px;color:#fff;margin-top:16px;letter-spacing:1px}
.contact p{font-size:11px;margin-top:8px}
.social-row{display:flex;align-items:center;justify-content:center;gap:14px;margin-top:44px;font-size:10px;letter-spacing:1px}
.social-row .rule{width:230px;height:1px;background:#444}
.social-row .dots{display:flex;gap:8px}
.social-row .dots span{width:16px;height:16px;border-radius:50%;background:#444;display:block}
.legal{text-align:center;margin-top:40px;font-size:10px}
.legal .mark{width:26px;height:26px;border-radius:50%;background:#555;margin:0 auto 10px}
.legal b{color:#fff}
.legal .links{margin-top:4px}
</style>
</head>
<body>

<div class="topbar">
  <div class="wrap">
    <span>(512) 607-4918</span>
    <span>2738 E 19th St #415 Austin, TX 78705</span>
    <span class="appt">Appointment Calendar</span>
    <div class="social"><span></span><span></span><span></span><span></span><span></span><span></span></div>
  </div>
</div>

<header class="header">
  <div class="brand-mark"></div>
  <div class="brand-name">Tessa Lorvel</div>
</header>

<nav class="nav">
  <ul>
    <li class="active">HOME</li><li>PROGRAMS</li><li>BLOG</li><li>MEET YOUR TRAINER</li><li>CONTACT ME</li><li class="cta">FREE SESSION!</li>
  </ul>
</nav>

<section class="hero" role="img" aria-label="Photo of an athlete lifting a heavy barbell in a dark gym">
  <div class="arrow l"></div><div class="arrow r"></div>
  <div class="copy">
    <h1>AUSTIN'S NO1 PERSONAL TRAINER !</h1>
    <div class="sub">Workouts Custom Tailored To You...</div>
    <span class="btn">Get Started Today !</span>
  </div>
  <div class="dots"><span class="on"></span><span></span><span></span></div>
</section>

<section class="get-started">
  <div class="sec-title"><span class="rule"></span><h2>GET STARTED TODAY !</h2><span class="rule"></span></div>
  <div class="sec-sub">Your First Sessions is Free!</div>
  <div class="features">
    <div class="feature"><div class="label">General<b>Fitness</b></div><div class="bowl"><svg width="26" height="26" viewBox="0 0 26 26"><circle cx="13" cy="13" r="10" fill="none" stroke="#fff" stroke-width="2"/><path d="M8 13h10" stroke="#fff" stroke-width="2"/></svg></div></div>
    <div class="feature"><div class="label">Strength<b>Training</b></div><div class="bowl"><svg width="26" height="26" viewBox="0 0 26 26"><path d="M6 18c4-2 6-8 6-12 4 2 7 6 8 12z" fill="none" stroke="#fff" stroke-width="2"/></svg></div></div>
    <div class="feature"><div class="label">Power<b>Lifting</b></div><div class="bowl"><svg width="30" height="26" viewBox="0 0 30 26"><path d="M4 13h22M7 7v12M10 9v8M23 7v12M20 9v8" stroke="#fff" stroke-width="2"/></svg></div></div>
    <div class="feature"><div class="label">Weight<b>Loss</b></div><div class="bowl"><svg width="26" height="26" viewBox="0 0 26 26"><path d="M13 3v20M7 8h12M9 8l-3 8h6zM17 8l-3 8h6z" fill="none" stroke="#fff" stroke-width="2"/></svg></div></div>
  </div>
  <div class="center"><span class="btn">Sign Up Today !</span></div>
</section>

<section class="services">
  <div class="sec-title"><span class="rule"></span><h2>TESSA LORVEL SERVICES !</h2><span class="rule"></span></div>
  <p class="intro">This is my training log for yesterday's workout! When finishing this workout you will have an awesome upper body pump for the rest of the day.</p>
  <div class="tabs"><span class="on">ALL</span><span>GENERAL FITNESS</span><span>STRENGTH TRAINING</span><span>POWER LIFTING</span><span>WEIGHT LOSS</span></div>
  <div class="wrap cards">
    <div class="card">
      <div class="ph" role="img" aria-label="Photo of a trainer coaching a client with weights" style="background:linear-gradient(135deg,#c9a48c,#6d7e9a)"></div>
      <h3>1-ON-1 PERSONAL TRAINING</h3>
      <p>This is my training log for yesterday's work out! When finishing this work...</p>
      <div class="facts"><span><i></i>Holistic Approach</span><span><i></i>Fast Result</span><span><i></i>Nutrition Advice</span><span><i></i>Weight Watch</span></div>
    </div>
    <div class="card">
      <div class="ph" role="img" aria-label="Photo of a woman stretching on a blue exercise mat" style="background:linear-gradient(135deg,#e8e6e2,#7bb6d6)"></div>
      <h3>ONLINE COACHING</h3>
      <p>This is my training log for yesterday's work out! When finishing this work...</p>
      <div class="facts"><span><i></i>Holistic Approach</span><span><i></i>Fast Result</span><span><i></i>Nutrition Advice</span><span><i></i>Weight Watch</span></div>
    </div>
    <div class="card">
      <div class="ph" role="img" aria-label="Photo of a group training with dumbbells in a studio" style="background:linear-gradient(135deg,#d23a5a,#8a5a4a)"></div>
      <h3>STRENGTH PROGRAMMING</h3>
      <p>This is my training log for yesterday's work out! When finishing this work...</p>
      <div class="facts"><span><i></i>Holistic Approach</span><span><i></i>Fast Result</span><span><i></i>Nutrition Advice</span><span><i></i>Weight Watch</span></div>
    </div>
  </div>
  <div class="center"><span class="btn">Read More Info !</span></div>
</section>

<section class="testimonials">
  <h2>TESTIMONIALS</h2>
  <p>Train hard and see real change. Every session was planned around my goals and my schedule, and I feel stronger than ever before. Highly recommended to anyone ready to start. <b>READ MORE</b></p>
  <div class="who"><span>CEO</span><span class="av"></span><span>TESSA LORVEL</span></div>
</section>

<section class="touch">
  <div class="sec-title"><span class="rule"></span><h2>KEEP IN TOUCH !</h2><span class="rule"></span></div>
  <div class="sec-sub">Keep In Touch With Tessa Lorvel</div>
  <div class="widgets">
    <div class="widget">
      <div class="bar">Like Me on Social Page</div>
      <div class="posttxt"><b>Tessa Lorvel</b><br>Day 4 of a 30 day challenge. Great work from everyone in the morning group!</div>
      <div role="img" aria-label="Before and after progress photo" style="height:120px;margin:0 10px;background:linear-gradient(135deg,#c69b7b,#5d4a3e)"></div>
    </div>
    <div class="widget">
      <div class="stats"><div><b>2981</b><span>Posts</span></div><div><b>947</b><span>Followers</span></div><div><b>437</b><span>Following</span></div></div>
      <div class="grid" role="img" aria-label="Grid of recent training photos">
        <div style="background:#b59a86"></div><div style="background:#6f7f8f"></div><div style="background:#a47a66"></div>
        <div style="background:#8d8d8d"></div><div style="background:#c6a995"></div><div style="background:#5f6d7a"></div>
      </div>
    </div>
    <div class="widget">
      <div class="bar feed">Photo Feed</div>
      <div class="grid" role="img" aria-label="Photo feed of fitness selfies">
        <div style="background:#c8ab98;height:70px"></div><div style="background:#9a8676;height:70px"></div><div style="background:#7a8aa0;height:70px"></div>
        <div style="background:#d1b5a2;height:70px"></div><div style="background:#8f7463;height:70px"></div><div style="background:#b9a393;height:70px"></div>
      </div>
    </div>
  </div>
</section>

<section class="blog">
  <div class="sec-title"><span class="rule"></span><h2>LATEST BLOG POSTS !</h2><span class="rule"></span></div>
  <div class="sec-sub">Read Tessa Lorvel Recent Blog Posts !</div>
  <div class="wrap post">
    <div class="ph" role="img" aria-label="Photo of a boxing training session with gloves"></div>
    <div>
      <div class="meta"><span class="av"></span><span>Written by <b>Tessa Lorvel</b> on 16 June 2015</span></div>
      <div class="stats"><div><b>12</b><span>Likes</span></div><div><b>8</b><span>Comments</span></div><div><b>3</b><span>Shares</span></div></div>
      <h3>TRAIN WITH TESSA LORVEL!</h3>
      <p>Hi there! I have been training clients for over ten years and every plan starts with a simple talk about your goals. In this post I share the routine that helps busy people build strength in just three short sessions a week. Let's get you moving.</p>
      <div class="more">Continue Reading...</div>
    </div>
  </div>
  <div class="wrap thumbs" role="img" aria-label="Row of recent blog post photos of gym workouts">
    <div style="background:#a8826a"></div><div style="background:#9c3b3b"></div><div style="background:#6e7e90"></div><div style="background:#c4a289"></div><div style="background:#7ba8c8"></div>
  </div>
  <div class="center"><span class="btn">Read More Blogs !</span></div>
</section>

<section class="join">
  <div class="band">
    <h2>JOIN US TODAY !</h2>
    <div class="items"><span><i></i>General Fitness</span><span><i></i>Strength Training</span><span><i></i>Power Lifting</span><span><i></i>Weight Loss</span></div>
  </div>
  <div class="center"><span class="btn">Get Started Today !</span></div>
</section>

<footer class="footer">
  <div class="tags">
    <span>MOTIVATION</span><span>WHAT NOW MOVES</span><span>TIPS</span><span>WORKOUT TIPS</span><span>MOTIVATION</span><span>WORKOUT</span>
    <span>WORKING TRAINING LOSS</span><span>WORKOUT TIPS</span><span>TIPS</span><span>WORKING TRAINING LOSS</span><span>WHAT NOW MOVES</span><span>TIPS</span>
  </div>
  <div class="contacts">
    <div class="contact"><div class="ic"><svg width="26" height="26" viewBox="0 0 24 24"><path d="M6 3l3 4-2 2c1 3 4 6 7 7l2-2 4 3-2 3C10 20 4 14 3 5z" fill="none" stroke="#ccc" stroke-width="1.6"/></svg></div><h4>PHONE</h4><p>(512) 607-4918</p></div>
    <div class="contact"><div class="ic"><svg width="26" height="26" viewBox="0 0 24 24"><path d="M12 22s7-7 7-12a7 7 0 0 0-14 0c0 5 7 12 7 12z" fill="none" stroke="#ccc" stroke-width="1.6"/><circle cx="12" cy="10" r="2.5" fill="none" stroke="#ccc" stroke-width="1.6"/></svg></div><h4>ADDRESS</h4><p>2738 E 19th St #415 Austin, TX 78705</p></div>
    <div class="contact"><div class="ic"><svg width="26" height="26" viewBox="0 0 24 24"><rect x="3" y="6" width="18" height="12" fill="none" stroke="#ccc" stroke-width="1.6"/><path d="M3 6l9 7 9-7" fill="none" stroke="#ccc" stroke-width="1.6"/></svg></div><h4>EMAIL</h4><p>info@tessalorvel.com, support@tessalorvel.com</p></div>
  </div>
  <div class="social-row"><span>SOCIAL</span><span class="rule"></span><div class="dots"><span></span><span></span><span></span><span></span><span></span></div><span class="rule"></span><span>KEEP IN TOUCH</span></div>
  <div class="legal">
    <div class="mark"></div>
    Copyright © 2015 - <b>Tessa Lorvel</b> - All Rights Reserved.
    <div class="links">Terms &amp; Conditions &nbsp;|&nbsp; Site Map &nbsp;|&nbsp; Privacy Policy</div>
  </div>
</footer>

</body>
</html>
```